Inspiring book cover design (business book for designers and innovators)

I'm writing my first book, to be published early next year. I'm struggling to come up with an inspiring book cover design. I need your help!

Information to be included on the cover:
Book Title: Bright maker's manual
Subtitle: Designing products and services that make sense
Author: Marianne Colt
Optional (not sure yet if I should include this on the cover): with online toolset

The book will be a square, size 170 x 170 mm
In the uploaded file you can find some example pages from the inside of the book. The cover design should fit with the design style of the example pages. The cover should "jump out" from the shelve in a bookstore and should attract designers, innovators, product managers, developers, and startup founders to buy the book.
Publisher: www.quillmarkpress.example

About the book:
Why do some products fail while others become a success? Why do so many companies launch crappy products and services that nobody wants? This book is both a guide to and a source of inspiration for, designing products and services that make sense. Because if they make sense to people, people will want them.
In order for tech products and services to make sense, and create value for users, we need to apply technologies in a meaningful way. We can achieve this by designing strong benefits and at the same time minimizing resistance users might have against new technologies.
This book offers a complete overview of how to develop products and services that make sense: 27 ways to strengthen benefits and 28 ways to mitigate resistance. It offers practical insights, examples, tips, and tools to design products and services that people will love to use.

About the author:
https://www.linkedin.example/in/mariannecolt/

Target Market(s)

designers, innovators, product managers, developers, and startup founders

Industry/Entity Type

Design Agency

Font styles to use
Other font styles liked:
• You can choose. The inside of the book uses 3 fonts: LuloCleanW01-OneBold, Sansation, Segoe UI

Requirements
Must have
• Clean, yet creative design.
Square shape
Fits the design style of the example pages
Sans serif fonts. Do not have to be the same fonts like the ones that are used inside the book (LuloCleanW01-OneBold, Sansation, Segoe UI), but should go well with them.

Bright makers manual
55 ways to design products and services that make sense
Marianne Colt
Nice to have
• I have several ideas that you might take as a starting point:
1) Do something with the left brain (rational, more digital) - right brain (creative, more emotional). For products to make sense, it needs to appeal to both parts of the brain
2) Work with a pattern, for example a (polygonal) triangular pattern
3) playful element in the letters, for example turning the O in innovator's into an on-off button or a stylish smiley, flipping the N in innovator's, doing something playful with the ' in innovator's
I've uploaded some images as a source of inspiration.

The cover should have a different color than the red/blue used in the example pages, but should fit the color palette that is used in the example pages.
Trigger curiosity.
Should not have
• Photographic pictures

```html
<!DOCTYPE html>
<html lang="en">
<head>
<meta charset="utf-8">
<title>Bright makers manual — book cover</title>
<link rel="stylesheet" href="https://fonts.googleapis.com/css2?family=Montserrat:wght@700;800;900&family=Open+Sans:wght@600;700&display=swap">
<style>
  :root {
    --backdrop: #262626;
    --paper: #efefef;
    --paper-light: #f7f7f7;
    --ink: #0d0d0d;
    --teal: #3fa9c1;
    --teal-badge: #56b6cb;
    --subtitle: #474747;
    --white: #ffffff;
    --bulb-yellow: #f6e24a;
    --bulb-shade: #e9cf2a;
  }
  * { margin: 0; padding: 0; box-sizing: border-box; }
  html, body { width: 1200px; height: 1200px; overflow: hidden; background: var(--backdrop); }
  .canvas { position: relative; width: 1200px; height: 1200px; background: var(--backdrop); }
  .cover {
    position: absolute; left: 218px; top: 26px; width: 764px; height: 1146px;
    background: radial-gradient(ellipse at 50% 25%, var(--paper-light) 0%, var(--paper) 60%);
    overflow: hidden;
  }
  .bulb-illustration {
    position: absolute; left: 178px; top: 88px; width: 402px; height: 372px;
    background: radial-gradient(circle at 50% 40%, var(--bulb-yellow) 0%, var(--bulb-shade) 28%, rgba(239,239,239,0) 52%);
  }
  .toolset-badge {
    position: absolute; left: 568px; top: 16px; width: 180px; height: 180px;
    border-radius: 50%; background: var(--teal-badge);
    border: 5px solid var(--white); box-shadow: 0 0 0 2px var(--teal-badge);
    display: flex; align-items: center; justify-content: center;
  }
  .toolset-badge__text {
    font-family: "Montserrat", sans-serif; font-weight: 800; font-size: 25px; line-height: 1.05;
    color: var(--white); text-align: center; transform: rotate(18deg);
    letter-spacing: 0.5px;
  }
  .title-line {
    position: absolute; left: 0; width: 100%; text-align: center;
    font-family: "Montserrat", sans-serif; line-height: 1; white-space: nowrap;
  }
  .title-line--first { top: 504px; font-size: 150px; font-weight: 900; color: var(--ink); letter-spacing: -3px; }
  .title-line--accent { top: 654px; font-size: 103px; font-weight: 800; color: var(--teal); letter-spacing: -1px; }
  .title-line--last { top: 738px; font-size: 145px; font-weight: 900; color: var(--ink); letter-spacing: -3px; }
  .title-rule {
    position: absolute; left: 76px; top: 892px; width: 612px; height: 3px;
    background: linear-gradient(90deg, rgba(63,169,193,0) 0%, var(--teal) 50%, rgba(63,169,193,0) 100%);
  }
  .subtitle {
    position: absolute; left: 0; top: 918px; width: 100%; text-align: center;
    font-family: "Open Sans", sans-serif; font-weight: 700; font-size: 27px; line-height: 40px;
    color: var(--subtitle);
  }
  .author-band {
    position: absolute; left: 0; top: 1032px; width: 100%; height: 80px;
    background: var(--teal);
    display: flex; align-items: center; justify-content: center;
    font-family: "Montserrat", sans-serif; font-weight: 800; font-size: 47px; letter-spacing: 5px;
  }
  .author-band__first { color: var(--ink); }
  .author-band__last { color: var(--white); margin-left: 22px; }
</style>
</head>
<body>
<main class="canvas">
  <section class="cover">
    <div class="bulb-illustration" role="img" aria-label="Illustration of a crumpled yellow paper ball forming a light bulb with drawn rays and screw base"></div>
    <div class="toolset-badge"><p class="toolset-badge__text">WITH<br>ONLINE<br>TOOLSET</p></div>
    <h1 class="book-title">
      <span class="title-line title-line--first">BRIGHT</span>
      <span class="title-line title-line--accent">MAKERS</span>
      <span class="title-line title-line--last">MANUAL</span>
    </h1>
    <div class="title-rule"></div>
    <p class="subtitle">Designing products<br>and services that make sense</p>
    <div class="author-band"><span class="author-band__first">MARIANNE</span><span class="author-band__last">COLT</span></div>
  </section>
</main>
</body>
</html>
```